Computer repair shop

A card with our logo. And number and email and address. Our colors are baby /light blue and gray

Prefferably one sode with full logo - interested in other designs and options

Computer / mac repair shop
On site support
Snall business IT support

```html
<!DOCTYPE html>
<html lang="en">
<head>
<meta charset="utf-8">
<title>ByteMend Repair – Business Card</title>
<link rel="stylesheet" href="https://fonts.googleapis.com/css2?family=Open+Sans:wght@300;400;600&family=Noto+Serif:ital@1&display=swap">
<style>
  :root {
    --backdrop: #e8e6e2;
    --card-white: #fbfbfb;
    --ink: #3a3a3a;
    --ink-soft: #4a4a4a;
    --baby-blue: #4aa3dc;
    --blue-light: #63b2e2;
    --blue-deep: #3d8fc9;
    --frame-gray: #5c595a;
    --logo-gray: #2f3236;
  }
  * { box-sizing: border-box; margin: 0; padding: 0; }
  html, body { width: 1200px; height: 942px; overflow: hidden; }
  body {
    background: var(--backdrop);
    font-family: "Open Sans", Arial, sans-serif;
    position: relative;
  }
  .card {
    position: absolute;
    left: 220px;
    width: 760px;
    height: 434px;
    border-radius: 4px;
    box-shadow: 0 6px 18px rgba(0,0,0,0.18);
    overflow: hidden;
  }
  /* Front */
  .card--front { top: 26px; background: var(--card-white); }
  .brand {
    position: absolute;
    left: 60px;
    top: 180px;
    display: flex;
    align-items: center;
    gap: 14px;
  }
  .brand__dot {
    width: 30px; height: 30px;
    border-radius: 50%;
    background: var(--baby-blue);
  }
  .brand__name {
    font-weight: 600;
    font-size: 30px;
    color: var(--logo-gray);
    letter-spacing: 0.5px;
  }
  .contact {
    position: absolute;
    left: 410px;
    top: 98px;
    color: var(--ink);
  }
  .contact__name {
    font-weight: 300;
    font-size: 31px;
    letter-spacing: 0.5px;
    line-height: 1.1;
  }
  .contact__title {
    font-family: "Noto Serif", Georgia, serif;
    font-style: italic;
    font-size: 17px;
    color: var(--baby-blue);
    margin-top: 2px;
  }
  .contact__list { list-style: none; margin-top: 16px; }
  .contact__item {
    display: flex; align-items: center; gap: 12px;
    font-size: 17px; color: var(--ink-soft);
    height: 30px;
  }
  .contact__icon { width: 16px; height: 16px; flex: none; }
  .contact__address {
    margin-top: 22px;
    font-size: 17px;
    line-height: 1.55;
    color: var(--ink-soft);
  }
  /* Back */
  .card--back {
    top: 482px;
    background: var(--frame-gray);
    padding: 22px;
  }
  .back__panel {
    position: relative;
    width: 100%; height: 100%;
    background: linear-gradient(160deg, var(--blue-light), var(--blue-deep));
  }
  .back__services {
    position: absolute;
    left: 14px; top: 12px;
    font-size: 15px;
    font-weight: 400;
    color: #ffffff;
    letter-spacing: 0.3px;
    word-spacing: 1px;
  }
  .back__services .sep { margin: 0 10px; }
  .back__mascot {
    position: absolute;
    left: 250px; top: 70px;
    width: 430px; height: 300px;
    border-radius: 40px;
    background: radial-gradient(ellipse at center, rgba(255,255,255,0.35), rgba(255,255,255,0.05) 70%);
  }
</style>
</head>
<body>
  <section class="card card--front">
    <div class="brand">
      <span class="brand__dot"></span>
      <span class="brand__name">ByteMend Repair</span>
    </div>
    <div class="contact">
      <h1 class="contact__name">YOUR NAME</h1>
      <p class="contact__title">Job Title</p>
      <ul class="contact__list">
        <li class="contact__item">
          <svg class="contact__icon" viewBox="0 0 16 16"><path fill="#4aa3dc" d="M3.5 1.5l2.5 0 1 3.5-1.6 1.2c.8 1.8 2.2 3.2 4 4l1.2-1.6 3.5 1v2.5c0 .8-.7 1.5-1.5 1.4C7 13 3 9 2 3c-.1-.8.6-1.5 1.5-1.5z"/></svg>
          +1 (253) 555-0142
        </li>
        <li class="contact__item">
          <svg class="contact__icon" viewBox="0 0 16 16"><rect x="1" y="3" width="14" height="10" rx="1" fill="#4aa3dc"/><path d="M1.5 3.5L8 9l6.5-5.5" fill="none" stroke="#fff" stroke-width="1.2"/></svg>
          service@bytemendrepair.com
        </li>
        <li class="contact__item">
          <svg class="contact__icon" viewBox="0 0 16 16"><circle cx="8" cy="8" r="6.5" fill="#4aa3dc"/><path d="M1.5 8h13M8 1.5c-2.5 3-2.5 10 0 13M8 1.5c2.5 3 2.5 10 0 13" fill="none" stroke="#fff" stroke-width="0.9"/></svg>
          www.bytemendrepair.com
        </li>
      </ul>
      <p class="contact__address">4820 SE Alder St #112<br>Cedar Hollow WA 98021</p>
    </div>
  </section>

  <section class="card card--back">
    <div class="back__panel">
      <p class="back__services">Computer / mac repair shop<span class="sep">I</span>On site support<span class="sep">I</span>Small business IT support</p>
      <div class="back__mascot" role="img" aria-label="Cheerful cartoon mascot illustration in white and blue"></div>
    </div>
  </section>
</body>
</html>
```